Website for Vicuna Dreamrest
showcasing 2 products: Vicuna Snugnest & Vicuna Velvetine
Website for Vicuna Dreamrest - Handmade Crafts
Creative Brief
Handmade Crafts
Our company sells hand made products from the alpaca wool. Now we need a website to introduce our company and showcase our products. We need to be able to change existing texts and pictures our self. We need a tab to introduce our company, our 2 main products, contact and one additional one where we are going to link the web shop to. We have two main products: 1. Vicuno Snugnest: Duvet filled with Alpaca wool 2. Wool blankets made form Baby Alpaca wool is named Vicuna Velvetine. Company: VICUNA DREAMREST: All our products are hand made and crafted by artisans. Alpaca wool has 3 main unique qualities: 1. It is hypoallergenic - which means that even people with severe animal hair allergies have no problem with this type of wool. 2. No animal has to die in order to get the wool. (Unlike feathers etc.) 3. It is temperature regulating, granting a good sleep despite cold or hot temperatures. The wool is one of the most expensive and exclusive on the market. Even in the past it was traded as a luxury good for kings and queens. It is even softer than Kashmir wool. But this aspect is not the only point we need the logo to convey. The point of it being yielded without harming an animal and its health benefits are our main selling points. The luxury aspect is not in the foreground for us. The alpaca is very good-natured animal and quite elegant in its way. The logo should reflect a certain elegance. The colours: We do not colorise out wool-blankets as the wool is worked in its naturally occurring colours: Black beige grey anthracite and white. The logo does not have to be in those exact colours but should consist of a natural colour scheme. This scheme will be then extended to the website design. I could imagine the Alpaca Animal being featured in the logo design in a schematic and/or abstract way. The company name: Vicuna Dreamrest should also be integrated. However, the symbol should also be able to stand on its own. Thank you so much for taking the time and I am looking forward to seeing your designs.
Please use the existing logos for colour reference. Please ready the brief and the company identity to create a feel on the page that expresses the nature of what we do.
Modern
Brown: Pantone 7532
Green: Pantone 378
left side
vicuna-dreamrest.example
vicuna-snugnest.example
vicuna-velvetine.example
Fonts used in Logo: Gill Sans MT Trojan Pro Bold Please also consider colours used in additional Logos: Black: Pantone Process Black (70%) Blue: Pantone 5405 Dark Green: Pantone 378 Dark Brown: Pantone 7532 Light Brown: Pantone 7504
SiteAdmin SiteAdmin
mirelatoskov mirelatoskov
#4 I like the colours in that draft. It's elegant. Thank you.
We do not have any product images yet. IS it not possible to insert them at a later stage?
We would like our page to look elegant and sleek.
Unfortunately, we do not have them yet.
TobiasWendlrup TobiasWendlrup

```html
<!DOCTYPE html>
<html lang="en">
<head>
<meta charset="utf-8">
<title>Vicuna Dreamrest</title>
<link rel="stylesheet" href="https://fonts.googleapis.com/css2?family=Lato:ital,wght@0,400;0,700;1,400&display=swap">
<style>
  :root {
    --page-bg: #efefeb;
    --panel: #ffffff;
    --green: #4f7d1e;
    --green-dark: #3a6112;
    --green-light: #6f9a34;
    --brown: #5a4a3a;
    --text: #6b6b6b;
    --caption: #4b4b4b;
    --beige: #d9cbb6;
    --cream: #f1ebe0;
    --grey: #a9a49c;
    --anthracite: #4a4744;
    --camel: #b8956a;
    --umber: #7a5e45;
  }
  * { margin: 0; padding: 0; box-sizing: border-box; }
  html, body { width: 1200px; height: 953px; overflow: hidden; }
  body {
    position: relative;
    background: var(--page-bg);
    font-family: "Lato", sans-serif;
    color: var(--text);
  }
  .site-header { position: absolute; left: 0; top: 0; width: 1200px; height: 98px; }
  .brand {
    position: absolute; left: 232px; top: 22px;
    font-weight: 700; font-size: 30px; line-height: 30px; letter-spacing: 1px;
    color: var(--brown);
  }
  .main-nav {
    position: absolute; left: 0; top: 98px; width: 1200px; height: 31px;
    background: linear-gradient(to bottom, var(--green-light), var(--green) 55%, var(--green-dark));
  }
  .main-nav a {
    position: absolute; top: 8px;
    font-size: 12px; color: #fff; text-decoration: none;
  }
  .content-panel {
    position: absolute; left: 180px; top: 129px; width: 850px; height: 796px;
    background: var(--panel);
    box-shadow: 0 0 6px rgba(0,0,0,0.12);
  }
  .hero {
    position: absolute; left: 5px; top: 13px; width: 825px; height: 180px;
    background: linear-gradient(90deg, var(--beige) 0%, var(--camel) 25%, var(--cream) 48%, var(--grey) 70%, var(--umber) 86%, var(--anthracite) 100%);
    box-shadow: 0 6px 8px rgba(0,0,0,0.25);
  }
  .feature-circle {
    position: absolute; top: 206px; width: 216px; height: 216px; border-radius: 50%;
    border: 5px solid #fff;
    box-shadow: 0 0 0 1px #d8d8d8, 0 4px 8px rgba(0,0,0,0.2);
  }
  .circle-yarn { left: 42px; background: radial-gradient(circle, var(--cream), var(--camel) 60%, var(--umber)); }
  .circle-beads { left: 309px; background: radial-gradient(circle, var(--beige), var(--grey) 60%, #8a857d); }
  .circle-knit { left: 587px; background: radial-gradient(circle, var(--cream), #6b625a 55%, var(--anthracite)); }
  .welcome-title {
    position: absolute; left: 16px; top: 450px;
    font-style: italic; font-weight: 400; font-size: 17px; color: var(--green);
  }
  .welcome-text {
    position: absolute; left: 16px; top: 475px; width: 818px;
    font-size: 11px; line-height: 18.5px; text-align: justify; letter-spacing: 0.4px;
  }
  .product-card { position: absolute; top: 600px; width: 243px; height: 177px; overflow: hidden; }
  .product-card .photo { position: absolute; inset: 0; }
  .card-one { left: 20px; }
  .card-one .photo { background: linear-gradient(135deg, var(--cream), var(--beige) 50%, var(--camel)); }
  .card-two { left: 299px; width: 237px; }
  .card-two .photo { background: linear-gradient(180deg, var(--anthracite), var(--grey) 40%, var(--beige) 70%, var(--cream)); }
  .card-three { left: 577px; width: 245px; }
  .card-three .photo { background: linear-gradient(180deg, var(--umber), var(--camel) 45%, var(--beige) 75%, var(--cream)); }
  .product-card .caption {
    position: absolute; left: 0; right: 0; bottom: 0; height: 32px;
    background: rgba(255,255,255,0.5);
    text-align: center; font-size: 15px; line-height: 32px; color: var(--caption);
  }
  .site-footer {
    position: absolute; left: 0; top: 927px; width: 1200px; height: 26px;
    background: linear-gradient(to bottom, var(--green-light), var(--green-dark));
  }
  .site-footer p {
    position: absolute; left: 186px; top: 7px; font-size: 9px; color: #e9f2dc;
  }
</style>
</head>
<body>
  <header class="site-header">
    <div class="brand">VICUNA<br>DREAMREST</div>
  </header>

  <nav class="main-nav">
    <a style="left:193px">Home</a>
    <a style="left:265px">About Us</a>
    <a style="left:355px">Services</a>
    <a style="left:443px">Consulting Services</a>
    <a style="left:577px">Products</a>
    <a style="left:662px">Contact Us</a>
  </nav>

  <main class="content-panel">
    <div class="hero" role="img" aria-label="Banner photo of knitted wool, scarves and folded sweaters"></div>

    <div class="feature-circle circle-yarn" role="img" aria-label="Photo of yarn crafts"></div>
    <div class="feature-circle circle-beads" role="img" aria-label="Photo of hands working on a craft"></div>
    <div class="feature-circle circle-knit" role="img" aria-label="Photo of a knitted pattern"></div>

    <h1 class="welcome-title">Welcome To VICUNA DREAMREST</h1>
    <p class="welcome-text">Every blanket and duvet we offer is made by hand from natural alpaca fibre, worked in its own undyed shades of black, beige, grey, anthracite and white. The wool is soft, light and kind to the skin, so even people with strong hair allergies can rest well beneath it. No animal is harmed to gather it; the fleece is shorn gently each year and the herd lives long and calm lives in the highlands. Because the fibre regulates warmth, it keeps you cosy on cold nights and cool when the air turns warm. Our artisans spin, weave and finish each piece slowly, with care for every seam and edge, so that it lasts for many years of quiet, deep and healthy sleep. Discover our duvet and our baby alpaca blankets, and feel the difference natural wool can make in your home.</p>

    <div class="product-card card-one">
      <div class="photo" role="img" aria-label="Photo of rolled wool"></div>
      <div class="caption">Vicuno Snugnest</div>
    </div>
    <div class="product-card card-two">
      <div class="photo" role="img" aria-label="Photo of stacked folded wool blankets"></div>
      <div class="caption">Vicuna Velvetine</div>
    </div>
    <div class="product-card card-three">
      <div class="photo" role="img" aria-label="Photo of stacked knitted wool pieces"></div>
      <div class="caption">Vicuno Snugnest</div>
    </div>
  </main>

  <footer class="site-footer">
    <p>© 2013 Vicuna Dreamrest | Handmade Crafts</p>
  </footer>
</body>
</html>
```